Packaging Design for Vanta Core

We require an outstanding packaging design for our Vanta Core brand, which offers hydration electrolyte supplements specifically tailored for athletes and sporty individuals.

Benchmark packaging design from liquora competitor attached. The product packaging contains 20 x 20g sticks of the product.

Target Market

Psychographic: Health-conscious, active lifestyle, values quality, functionality and sustainability.

product description 1:
HYDRATION BOOSTER
Refresh, Replenish, Recharge!

product description 2:
PREMIUM ISOTONIC ELECTROLYTE DRINK
Nutritional Expertise Since 1992.

Existing Logo: to add "since 1992"

Appeal to Target Market: Create a design that resonates with both men and women in the 25-55 age group.

Grafik Design: Develop a visually striking design that grabs attention in online retail environments like Brindle.

Visuals: glass of water (or symbolic) and sticks (powder) just like benchmark brand liquora.

Design Elements
Use colours that are inside the Vanta-Core Logo, attached.
Product will be available in 3 flavours. Lemon=yellow, Orange=orange, Black Currant=purple

Typography: Utilize strong, clean, and modern fonts. Ensure readability and create a sense of strength, endurance and reliability.

The product will be available in 3 flavours: Lemon, Orange and Johannisbeere

We look forward to seeing your creative ideas and innovative designs for our Vanta Core brand packaging.

```html
<!DOCTYPE html>
<html lang="en">
<head>
<meta charset="utf-8">
<title>Vanta Core — Hydration Booster Packaging</title>
<link rel="stylesheet" href="https://fonts.googleapis.com/css2?family=Outfit:wght@400;500;600;700;800&display=swap">
<style>
  :root {
    --canvas: #e0e0e0;
    --brand-blue: #22408f;
    --brand-yellow: #fff100;
    --brand-pink: #d41f74;
    --white: #ffffff;
  }
  html, body { margin: 0; padding: 0; width: 1200px; height: 600px; overflow: hidden; background: var(--canvas); }
  .artboard { display: block; width: 1200px; height: 600px; }
  .type { font-family: "Outfit", sans-serif; }
  .pack--lemon  { --bg: url(#bg-lemon);  --accent: var(--brand-yellow); --footer: #137a3c; --feature: #0b6b30; --pill: var(--brand-yellow); --pill-text: #0b6b30; --stick-bg: #137a3c; --stick-sub: var(--brand-yellow); }
  .pack--currant{ --bg: url(#bg-currant);--accent: #d6138c; --footer: #3c1a55; --feature: #b23a92; --pill: #d6138c; --pill-text: #4a0f5e; --stick-bg: #3f1653; --stick-sub: #d6138c; }
  .pack--orange { --bg: url(#bg-orange); --accent: #fdb913; --footer: #ee4322; --feature: #ee4322; --pill: #fdb913; --pill-text: #ee4322; --stick-bg: #ef4323; --stick-sub: var(--brand-yellow); }
  .fill-bg { fill: var(--bg); }
  .fill-accent { fill: var(--accent); }
  .fill-footer { fill: var(--footer); }
  .fill-feature { fill: var(--feature); }
  .fill-pill { fill: var(--pill); }
  .fill-pill-text { fill: var(--pill-text); }
  .fill-stick { fill: var(--stick-bg); }
  .fill-stick-sub { fill: var(--stick-sub); }
  .fill-blue { fill: var(--brand-blue); }
  .fill-yellow { fill: var(--brand-yellow); }
  .fill-pink { fill: var(--brand-pink); }
  .fill-white { fill: var(--white); }
  .count { font-weight: 800; }
  .brand-name { font-weight: 800; fill: var(--brand-yellow); }
  .headline { font-weight: 700; fill: var(--white); }
  .tagline { font-weight: 700; }
  .subhead { font-weight: 700; fill: var(--white); }
  .feature { font-weight: 500; }
  .footer-line { font-weight: 500; fill: var(--white); letter-spacing: 4px; }
  .small { font-weight: 500; }
</style>
</head>
<body>
<svg class="artboard type" viewBox="0 0 2576 1288" xmlns="http://www.w3.org/2000/svg" role="group" aria-label="Vanta Core Hydration Booster packaging in Lemon, Blackcurrant and Orange">
  <defs>
    <linearGradient id="bg-lemon" x1="0" y1="0" x2="0" y2="1">
      <stop offset="0.35" stop-color="#06893d"/><stop offset="0.62" stop-color="#27a83f"/><stop offset="1" stop-color="#eaea3a"/>
    </linearGradient>
    <linearGradient id="bg-currant" x1="0" y1="0" x2="0" y2="1">
      <stop offset="0.35" stop-color="#3a0a50"/><stop offset="0.65" stop-color="#6a1a78"/><stop offset="1" stop-color="#b3208a"/>
    </linearGradient>
    <linearGradient id="bg-orange" x1="0" y1="0" x2="0" y2="1">
      <stop offset="0.35" stop-color="#f04523"/><stop offset="0.65" stop-color="#f57a22"/><stop offset="1" stop-color="#f9ab25"/>
    </linearGradient>
    <linearGradient id="glass-fill" x1="0" y1="0" x2="0" y2="1">
      <stop offset="0" stop-color="#ffffff" stop-opacity="0.25"/><stop offset="0.6" stop-color="#ffffff" stop-opacity="0.45"/><stop offset="1" stop-color="#ffffff" stop-opacity="0.2"/>
    </linearGradient>
    <linearGradient id="stream-fill" x1="0" y1="0" x2="0" y2="1">
      <stop offset="0" stop-color="#ffffff" stop-opacity="0.4"/><stop offset="1" stop-color="#ffffff" stop-opacity="0.85"/>
    </linearGradient>

    <symbol id="box-front" viewBox="0 0 710 792">
      <rect class="fill-bg" width="710" height="792"/>
      <path class="fill-footer" d="M0 745 Q355 690 710 740 V792 H0Z"/>
      <g role="img" aria-label="Glass of water with electrolyte powder pouring into it">
        <path fill="url(#glass-fill)" d="M405 480 Q532 465 660 480 L635 792 L440 792Z"/>
        <path fill="url(#stream-fill)" d="M530 290 L556 290 L566 640 L516 640Z"/>
      </g>
      <path class="fill-accent" d="M0 200 Q355 380 710 200 V222 Q355 410 0 222Z"/>
      <path class="fill-blue" d="M0 0 H710 V200 Q355 380 0 200Z"/>
      <rect class="fill-yellow" x="56" y="0" width="79" height="91"/>
      <text class="count fill-blue" x="95.5" y="58" font-size="52" text-anchor="middle">20</text>
      <text class="count fill-blue" x="95.5" y="80" font-size="17" text-anchor="middle">STICKS</text>
      <text class="small fill-white" x="56" y="112" font-size="10">NET WT 14.1oz / 400g</text>
      <circle class="fill-pink" cx="215" cy="195" r="34"/>
      <text class="brand-name" x="185" y="140" font-size="90">Vanta</text>
      <text class="brand-name" x="262" y="205" font-size="90">Core</text>
      <text class="small fill-white" x="486" y="222" font-size="17" transform="rotate(-14 486 222)">Since 1992</text>
      <text class="headline" x="56" y="401" font-size="63">HYDRATION</text>
      <text class="headline" x="56" y="461" font-size="63">BOOSTER</text>
      <text class="tagline fill-accent" x="57" y="496" font-size="19">REFRESH, REPLENISH &amp; RECHARGE!</text>
      <text class="subhead" x="57" y="568" font-size="31">PREMIUM ISOTONIC</text>
      <text class="subhead" x="57" y="605" font-size="31">ELECTROLYTE DRINK</text>
      <path class="fill-feature" d="M67 625 L58 647 H65 L61 664 L74 639 H67 L72 625Z"/>
      <text class="feature fill-feature" x="84" y="644" font-size="19">Fast Rehydration</text>
      <path class="fill-feature" d="M250 648 C238 645 237 632 243 626 C249 632 252 640 250 648Z M250 648 C262 645 263 632 257 626 C251 632 248 640 250 648Z M248 646 H252 V661 H248Z"/>
      <text class="feature fill-feature" x="270" y="644" font-size="19">Natural Flavors</text>
      <path class="fill-feature" d="M62 659 H69 V666 H76 V673 H69 V680 H62 V673 H55 V666 H62Z"/>
      <text class="feature fill-feature" x="84" y="675" font-size="19">Vitamins &amp; Minerals</text>
      <text class="footer-line" x="355" y="766" font-size="16" text-anchor="middle">NUTRITIONAL EXPERTISE SINCE 1992</text>
    </symbol>

    <symbol id="stick-front" viewBox="0 0 578 138">
      <rect class="fill-stick" width="578" height="138"/>
      <path class="fill-yellow" d="M448 0 H472 Q460 69 472 138 H448 Q436 69 448 0Z"/>
      <path class="fill-blue" d="M466 0 H578 V138 H466 Q454 69 466 0Z"/>
      <circle class="fill-pink" cx="500" cy="30" r="10"/>
      <text class="brand-name" font-size="24" transform="translate(520 22) rotate(68)">Vanta Core</text>
      <text class="small fill-white" font-size="9" transform="translate(30 108) rotate(-90)">NET WT 0.7oz / 20g</text>
      <rect class="fill-accent" x="40" y="18" width="20" height="102" rx="10"/>
      <text class="headline" x="80" y="55" font-size="29">HYDRATION BOOSTER</text>
      <text class="tagline fill-stick-sub" x="80" y="77" font-size="15">PREMIUM ISOTONIC ELECTROLYTE DRINK</text>
      <path class="fill-white" d="M86 93 L81 104 H85 L83 112 L90 100 H86 L89 93Z"/>
      <text class="feature fill-white" x="96" y="106" font-size="11">Fast Rehydration</text>
      <path class="fill-white" d="M204 104 C198 103 197 96 200 93 C203 96 205 100 204 104Z M204 104 C210 103 211 96 208 93 C205 96 203 100 204 104Z M203 103 H205 V111 H203Z"/>
      <text class="feature fill-white" x="217" y="106" font-size="11">Natural Flavors</text>
      <path class="fill-white" d="M311 96 H315 V100 H319 V104 H315 V108 H311 V104 H307 V100 H311Z"/>
      <text class="feature fill-white" x="326" y="106" font-size="11">Vitamins &amp; Minerals</text>
    </symbol>
  </defs>

  <rect width="2576" height="1288" fill="var(--canvas)"/>

  <g class="pack pack--lemon">
    <use href="#box-front" x="164" y="149" width="710" height="792"/>
    <rect class="fill-pill" x="428" y="850" width="181" height="34" rx="17"/>
    <text class="tagline fill-pill-text" x="518.5" y="874" font-size="19" text-anchor="middle">LEMON</text>
    <use href="#stick-front" x="229" y="1000" width="578" height="138"/>
    <text class="tagline fill-pill-text" font-size="11" text-anchor="middle" transform="translate(275 1069) rotate(90)">LEMON</text>
  </g>

  <g class="pack pack--currant">
    <use href="#box-front" x="933" y="149" width="710" height="792"/>
    <rect class="fill-pill" x="1197" y="850" width="181" height="34" rx="17"/>
    <text class="tagline fill-pill-text" x="1287.5" y="874" font-size="19" text-anchor="middle">BLACKCURRANT</text>
    <use href="#stick-front" x="999" y="1000" width="578" height="138"/>
    <text class="tagline fill-pill-text" font-size="9" text-anchor="middle" transform="translate(1045 1069) rotate(90)">BLACKCURRANT</text>
  </g>

  <g class="pack pack--orange">
    <use href="#box-front" x="1702" y="149" width="710" height="792"/>
    <rect class="fill-pill" x="1966" y="850" width="181" height="34" rx="17"/>
    <text class="tagline fill-pill-text" x="2056.5" y="874" font-size="19" text-anchor="middle">ORANGE</text>
    <use href="#stick-front" x="1768" y="1000" width="578" height="138"/>
    <text class="tagline fill-pill-text" font-size="11" text-anchor="middle" transform="translate(1814 1069) rotate(90)">ORANGE</text>
  </g>
</svg>
</body>
</html>
```